Financing Pitch Deck

PowerPoint presentation for meeting next week. Please include the Vestrel Logo, the Harrowick BI logo, and the KTX Pathfinder Logo. Recall, Anselm is an KTX pathfinder.
Please alter Slide 2 to read identify not identifies:

ZOR Text Modeling Algorithms employ randomness to Identify Distinctive Word Combinations

```html
<!DOCTYPE html>
<html lang="en">
<head>
<meta charset="utf-8">
<title>Vestrel Financing Pitch Deck 2021</title>
<link rel="stylesheet" href="https://fonts.googleapis.com/css2?family=Open+Sans:wght@300;400;600;700&display=swap">
<style>
:root{
  --bg:#eef0f3;
  --slide:#ffffff;
  --teal:#19a9b8;
  --teal-soft:#c9eef2;
  --navy:#1f3a6e;
  --sky:#2aa3de;
  --ink:#44505c;
  --muted:#7c8792;
  --shadow:rgba(20,40,70,.16);
}
*{box-sizing:border-box;margin:0;padding:0}
html,body{width:1200px;height:2192px;overflow:hidden}
body{background:var(--bg);font-family:"Open Sans",Arial,sans-serif;color:var(--ink);position:relative}
.slide{position:absolute;left:80px;width:1040px;height:392px;background:var(--slide);box-shadow:0 4px 16px var(--shadow);overflow:hidden}
.s1{top:36px}.s2{top:468px}.s3{top:900px}.s4{top:1332px}.s5{top:1764px}
.brand{position:absolute;display:flex;align-items:center;gap:8px;font-weight:600;font-size:19px;color:var(--teal)}
.brand i{width:14px;height:14px;border-radius:50%;background:var(--teal);display:block}
.pattern{position:absolute;inset:0;background:radial-gradient(ellipse at 20% 10%,#e3f4f7 0,transparent 55%),radial-gradient(ellipse at 80% 95%,#e6f1fa 0,transparent 55%)}
/* slide 1 */
.s1 .year{position:absolute;left:120px;top:98px;font-size:150px;font-weight:700;line-height:1;background:linear-gradient(90deg,#1b9fd8,#1cb5b0);-webkit-background-clip:text;background-clip:text;color:transparent;letter-spacing:-2px}
.s1 .divider{position:absolute;left:468px;top:110px;width:2px;height:150px;background:var(--teal)}
.s1 .brand{left:500px;top:92px;font-size:26px}
.s1 .brand i{width:20px;height:20px}
.s1 h1{position:absolute;left:500px;top:132px;font-size:52px;font-weight:700;color:var(--navy);line-height:1.05}
.s1 .sub{position:absolute;left:560px;top:262px;font-size:12px;color:var(--muted);text-align:center;line-height:1.4}
.badge{position:absolute;left:880px;width:70px;background:var(--navy)}
.badge.a{top:20px;height:72px}
.badge.b{top:110px;height:80px;background:#d9dde3}
/* slide 2 */
.s2 .brand{left:40px;top:24px}
.title{position:absolute;font-weight:300;line-height:1.05}
.s2 .title{left:40px;top:110px;font-size:62px;color:var(--teal)}
.band{position:absolute;left:0;top:190px;width:340px;height:3px;background:var(--teal)}
.s2 .lead{position:absolute;left:40px;top:220px;width:270px;font-size:22px;color:var(--sky);line-height:1.3}
.orb{position:absolute;top:24px;width:132px;height:132px;border-radius:50%;background:var(--teal);color:#fff;font-size:11px;text-align:center;display:flex;align-items:center;justify-content:center;padding:18px;line-height:1.35}
.orb.o1{left:646px}.orb.o2{left:800px}
.points{position:absolute;left:420px;top:200px;width:560px;list-style:none}
.points li{display:flex;gap:18px;align-items:flex-start;font-size:13px;color:var(--ink);margin-bottom:22px;line-height:1.4}
.points b{flex:none;width:28px;height:28px;border-radius:50%;background:var(--teal);color:#fff;font-size:13px;display:flex;align-items:center;justify-content:center}
/* slide 3 */
.s3 .brand{right:40px;top:24px}
.s3 .title{left:40px;top:48px;font-size:56px;color:var(--navy);width:860px}
.s3 .rule{position:absolute;left:40px;top:176px;width:960px;height:1px;background:#d6dbe0}
.claims{position:absolute;left:50px;top:206px;width:420px;list-style:none}
.claims li{display:flex;gap:18px;font-size:14px;line-height:1.4;margin-bottom:26px;color:var(--ink)}
.claims li::before{content:"";flex:none;width:24px;height:24px;border-radius:50%;background:var(--sky);margin-top:2px}
.allows{position:absolute;left:560px;top:206px;font-size:15px;color:var(--ink)}
.allows ul{margin-top:14px;padding-left:40px}
.allows li{margin-bottom:8px;font-size:17px}
/* slide 4 */
.s4 .brand{right:40px;top:24px}
.s4 .title{left:40px;top:96px;font-size:62px;color:var(--teal);line-height:1.12}
.algos{position:absolute;left:540px;top:64px;width:440px;list-style:none}
.algos li{position:relative;padding-left:28px;margin-bottom:16px;font-size:12px;line-height:1.4;color:var(--ink)}
.algos li::before{content:"";position:absolute;left:0;top:3px;width:16px;height:16px;border-radius:50%;background:var(--teal)}
.algos strong{display:block;font-size:15px;color:var(--navy)}
/* slide 5 */
.s5 .brand{left:40px;top:24px}
.s5 .title{left:40px;top:70px;font-size:52px;color:var(--navy)}
.s5 .rule{position:absolute;left:40px;top:140px;width:960px;height:1px;background:#d6dbe0}
.team{position:absolute;left:0;top:170px;width:1040px;display:flex;justify-content:center;gap:130px}
.member{width:170px;text-align:center}
.portrait{width:150px;height:150px;margin:0 auto;border-radius:50%;background:linear-gradient(160deg,#c9ccd1,#6f7a86)}
.member h3{margin-top:12px;font-size:13px;font-weight:600;color:var(--navy)}
.member p{font-size:10px;color:var(--muted);margin-top:2px}
</style>
</head>
<body>

<section class="slide s1">
  <div class="pattern" role="img" aria-label="Soft field of light teal dots decorating the title slide"></div>
  <div class="year">2021</div>
  <div class="divider"></div>
  <div class="brand"><i></i>Vestrel</div>
  <h1>Financing<br>Pitch Deck</h1>
  <p class="sub">Anselm Varholt, Vestrel Founder<br>Nov 19, 2021</p>
  <div class="badge a" role="img" aria-label="Harrowick BI partner badge"></div>
  <div class="badge b" role="img" aria-label="KTX Pathfinder badge"></div>
</section>

<section class="slide s2">
  <div class="brand"><i></i>Vestrel</div>
  <h2 class="title">Introduction</h2>
  <div class="band"></div>
  <p class="lead">ZOR has developed a collection of specialty algorithms which have the capacity to:</p>
  <div class="orb o1">Anselm Varholt is a KTX pathfinder and a noted expert in AI</div>
  <div class="orb o2">ZOR is a trusted partner to several data communities</div>
  <ol class="points">
    <li><b>1</b>Discover the dimensions of AI learning beyond artificial intelligence, towards the theoretical limits on which such algorithms currently depend.</li>
    <li><b>2</b>Derive benefit from the use of new models in a quantum environment.</li>
    <li><b>3</b>These abilities may make ZOR one of the most important technology companies in the world at present.</li>
  </ol>
</section>

<section class="slide s3">
  <div class="brand"><i></i>Vestrel</div>
  <h2 class="title">Why is ZOR Text Modelling Unique</h2>
  <div class="rule"></div>
  <ul class="claims">
    <li>ZOR Algorithms systematically employ randomness in multiple ways</li>
    <li>ZOR Text Modeling Algorithms employ randomness to Identify Distinctive Word Combinations</li>
  </ul>
  <div class="allows">This allows us to:
    <ul>
      <li>Detect weak signals in data,</li>
      <li>Train models efficiently, and</li>
      <li>Eliminate circuits of noise.</li>
    </ul>
  </div>
</section>

<section class="slide s4">
  <div class="brand"><i></i>Vestrel</div>
  <h2 class="title">Other<br>Notable<br>Algorithms</h2>
  <ul class="algos">
    <li><strong>Re Name Extraction—</strong>Identifies names of individuals in text with greater accuracy than rival extraction tools and at lower cost.</li>
    <li><strong>Data Lake Indexer—</strong>Indexes data and maintains speed regardless of the size of dataset processed and grows only linearly as the number of words per query grows, unlike rival indexing algorithms.</li>
    <li><strong>Back Propagation—</strong>Enables speed of training neural networks.</li>
  </ul>
</section>

<section class="slide s5">
  <div class="brand"><i></i>Vestrel</div>
  <h2 class="title">Leadership Team</h2>
  <div class="rule"></div>
  <div class="team">
    <div class="member">
      <div class="portrait" role="img" aria-label="Portrait photo of Brent Hallow"></div>
      <h3>Brent Hallow</h3>
      <p>Chief Executive Officer</p>
    </div>
    <div class="member">
      <div class="portrait" role="img" aria-label="Portrait photo of Dr. Anselm Varholt"></div>
      <h3>Dr. Anselm Varholt</h3>
      <p>Founder, Chief Technology Officer</p>
    </div>
    <div class="member">
      <div class="portrait" role="img" aria-label="Portrait photo of Conrad Ellery"></div>
      <h3>Conrad Ellery</h3>
      <p>Head of Finance and Operations</p>
    </div>
  </div>
</section>

</body>
</html>
```